Poster Design October

We are a Poker Club (Harlow Bay Veterans Cardroom Club). We run poker tournaments three night a week in Mount Gambier
We require a poster to advertise our upcoming major Poker tournament
The details of the event are set out below
ANNUAL $200 BUY IN TOURNAMENT
OCTOBER LONG WEEK END
4-5 OCTOBER 2014
$100K STARTING STACK
45 MIN BLINDS
HARLOW BAY VETERANS LEAGUE
27 DELLWYN STREET
KELVERTON SA 5371
10:00AM START (SA TIME)
REGISTRATION 9:30AM (SA TIME)
EMAIL HBVCARDS@MAILNEST.COM.AU FOR MORE INFORMATION
FIND US ON SOCIALINE: HBV CARDS 2014
I have attached a flyer this is something like what we are looking for
I Have also attached the HBV logo which need to be included
Poker plyers 18+ both genders
Club

```html
<!DOCTYPE html>
<html lang="en">
<head>
<meta charset="utf-8">
<title>Annual $200 Buy In Tournament – HBV Cards 2014</title>
<link href="https://fonts.googleapis.com/css2?family=Arimo:wght@700&family=Gochi+Hand&family=Rokkitt:wght@800&family=Montserrat:wght@700&display=swap" rel="stylesheet">
<style>
  :root{
    --page:#e9e4de;
    --poster-dark:#1c0703;
    --poster-mid:#7a2a0e;
    --poster-glow:#c8521c;
    --gold-top:#fff7a8;
    --gold-bottom:#f0c400;
    --cream:#fff1c2;
    --white:#ffffff;
    --sky:#a9e2ff;
    --black:#0b0b0b;
    --rust:#a8391b;
    --social-blue:#3b5998;
    --card-light:#f3ede6;
    --card-red:#c92a2a;
  }
  *{margin:0;padding:0;box-sizing:border-box}
  html,body{width:1200px;height:900px;overflow:hidden;background:var(--page)}
  .poster{
    position:absolute;left:342px;top:25px;width:564px;height:852px;overflow:hidden;
    background:radial-gradient(ellipse 70% 55% at 50% 45%,var(--poster-glow) 0%,var(--poster-mid) 45%,var(--poster-dark) 100%);
    text-align:center;
  }
  .line{position:absolute;left:0;width:100%;white-space:nowrap}
  .title{
    font-family:"Arimo",Arial,sans-serif;font-weight:700;font-size:40px;letter-spacing:.5px;
    background:linear-gradient(var(--gold-top),var(--gold-bottom));
    -webkit-background-clip:text;background-clip:text;color:transparent;
    filter:drop-shadow(2px 2px 2px rgba(0,0,0,.8));
  }
  .title-1{top:66px}
  .title-2{top:112px}
  .dates{font-family:"Gochi Hand",cursive;font-size:31px;color:var(--cream);line-height:1}
  .dates-1{top:186px}
  .dates-2{top:224px}
  .times{font-family:"Rokkitt",Georgia,serif;font-weight:800;color:var(--white);font-variant:small-caps;text-shadow:1px 1px 2px #000}
  .times-start{top:284px;font-size:30px}
  .times-reg{top:324px;font-size:26px}
  .stack{font-family:"Rokkitt",Georgia,serif;font-weight:800;font-size:36px;color:#f6d23c;text-shadow:2px 2px 3px #000}
  .stack-1{top:380px}
  .stack-2{top:426px}
  .venue{font-family:"Rokkitt",Georgia,serif;font-weight:800;font-size:24px;color:var(--white);letter-spacing:.6px;text-shadow:1px 1px 2px #000}
  .venue-1{top:494px}
  .venue-2{top:527px}
  .venue-3{top:561px}
  .email{top:635px;font-family:"Montserrat",Arial,sans-serif;font-weight:700;font-size:21px;color:var(--sky);letter-spacing:.5px;text-shadow:0 0 4px #3aa0ff,1px 1px 2px #000;padding-left:80px}
  .cards-art{
    position:absolute;left:16px;top:595px;width:310px;height:165px;
    background:linear-gradient(120deg,var(--card-light) 0%,#e0d6cb 55%,var(--card-red) 100%);
    border-radius:8px;opacity:.92;
  }
  .info-band{position:absolute;left:0;top:760px;width:100%;height:33px;background:var(--black)}
  .info-band span{position:absolute;left:24px;top:5px;font-family:"Montserrat",Arial,sans-serif;font-weight:700;font-size:18px;color:var(--white);letter-spacing:.5px}
  .social{position:absolute;left:0;top:793px;width:170px;height:59px;background:var(--white);
    font-family:"Montserrat",Arial,sans-serif;font-weight:700;font-size:24px;color:var(--social-blue);line-height:59px}
  .page-name{position:absolute;left:170px;top:793px;width:394px;height:59px;background:var(--rust);
    font-family:"Montserrat",Arial,sans-serif;font-weight:700;font-size:22px;color:var(--white);line-height:59px;text-align:left;padding-left:16px;letter-spacing:.5px}
  .club-mark{position:absolute;left:406px;top:700px;width:150px;height:150px}
  .club-mark text{font-family:"Montserrat",Arial,sans-serif;font-weight:700;font-size:26px}
</style>
</head>
<body>
<main class="poster">
  <h1 class="line title title-1">ANNUAL $200 BUY IN</h1>
  <h1 class="line title title-2">TOURNAMENT</h1>

  <p class="line dates dates-1">OCTOBER LONG WEEK END</p>
  <p class="line dates dates-2">4-5 OCTOBER 2014</p>

  <p class="line times times-start">10:00AM Start (SA Time)</p>
  <p class="line times times-reg">Registration 9:30AM (SA Time)</p>

  <p class="line stack stack-1">$100K STARTING STACK</p>
  <p class="line stack stack-2">45 MIN BLINDS</p>

  <p class="line venue venue-1">HARLOW BAY VETERANS LEAGUE</p>
  <p class="line venue venue-2">27 DELLWYN STREET</p>
  <p class="line venue venue-3">KELVERTON SA 5371</p>

  <div class="cards-art" role="img" aria-label="Fanned playing cards showing a royal flush in hearts"></div>

  <p class="line email">EMAIL: HBVCARDS@MAILNEST.COM.AU</p>

  <div class="info-band"><span>FOR MORE INFORMATION</span></div>
  <div class="social">Socialine</div>
  <div class="page-name">HBV CARDS 2014</div>

  <svg class="club-mark" viewBox="0 0 150 150" aria-label="HBV">
    <rect x="30" y="30" width="90" height="90" fill="#ffffff" stroke="#0b0b0b" stroke-width="3" transform="rotate(45 75 75)"/>
    <text x="75" y="84" text-anchor="middle" fill="#a8391b">HBV</text>
  </svg>
</main>
</body>
</html>
```